An expert for Professional and Technical Evaluation of Painting Work Needs a New Letterhead Design

I own a mid-sized painting company and also work as an expert for professional and technical evaluation of painting work in the area of Zurich.

Please read the project description and the must-have-requirements carefully!

I attached 1 PDF which will help you create a new letterhead design:

THE NEW DESIGN DOESN'T NEED A LOGO! (Because it won't represent a company, it represents only a service)
Updates

Dear designers We had a discussion about the location/placement of the design and came to the conclusion that we only want the design to be in the header area of the A4-paper. We would be glad to receive some revised version of your designs. Thank you and kind regards!

Project Deadline Extended
Reason: Due to the fact that only 20% of the designer have understood the brief and submitted designs that have met the requirements we decided to extend the contest deadline.

Project Deadline Extended
Reason: A great deal of good designs were submitted in the last few days. A big thank you to all the participating designers for your good work. We need a few more days to discuss some changes with certain designers and to decide which design will win.

Target Market(s)

(Insurance) Companies, partly also private clients.

Industry/Entity Type

Painting

Colors

Designer to choose colors to be used in the design.

Requirements
Must have
• All information (text, phone numbers, ...) of the old design ("old_letterhead_design.pdf") has also to be in the new one. Additional to that there are a few changes:
The phone numbers "01 583 61 47" and "01 583 61 37" change to "044 583 61 47" and "044 583 61 37". And please mention also this email address: gutachten@valmorkeller.example .

- The design should only be in the header-area of the A4-paper. An the background color of the A4-paper will be white.

- The design should consist of two designs. One for the first page and a smaller version of the design for the following pages.

- THE NEW DESIGN DOESN'T NEED A LOGO! You can make a design with geometric forms, ...

- The new design should have a juridical look. It should only contain colors like brown, fawn, black, light green, ...... colors which look serious/reliable.
Nice to have
• Geometric Forms, Symbols or other design elements.

- It would also be nice to have some design elements which emphasize the kind of work we are offering.

```html
<!DOCTYPE html>
<html lang="de">
<head>
<meta charset="utf-8">
<title>Valmor Keller – Briefpapier</title>
<link rel="stylesheet" href="https://fonts.googleapis.com/css2?family=Questrial&family=Arimo:wght@700&family=Raleway:wght@700&display=swap">
<style>
  :root {
    --paper: #ffffff;
    --name-red: #9b2b1f;
    --ink: #141414;
    --accent-red: #e02424;
    --rule: #7a7a7a;
    --hex-pink: #f08a86;
    --hex-pale: #fbd9d6;
    --dot-tint: #e9ece4;
  }
  * { margin: 0; padding: 0; box-sizing: border-box; }
  html, body { width: 900px; height: 1200px; overflow: hidden; background: var(--paper); }
  .letterhead { position: relative; width: 900px; height: 1200px; background: var(--paper); }

  .hex-pattern {
    position: absolute; left: 52px; top: 45px; width: 280px; height: 280px;
    background: radial-gradient(ellipse 95% 90% at 25% 25%, var(--hex-pink) 0%, var(--hex-pale) 55%, rgba(255,255,255,0) 80%);
    opacity: 0.55;
  }
  .dot-field {
    position: absolute; left: 430px; top: 45px; width: 408px; height: 200px;
    background: radial-gradient(ellipse 80% 100% at 100% 0%, var(--dot-tint) 0%, rgba(233,236,228,0.4) 55%, rgba(255,255,255,0) 85%);
  }

  .sender {
    position: absolute; right: 92px; top: 66px; text-align: right;
    font-family: "Questrial", "Century Gothic", sans-serif; font-size: 15.5px; color: var(--ink);
    line-height: 23.5px;
  }
  .sender-name {
    font-family: "Raleway", "Century Gothic", sans-serif; font-weight: 700;
    font-size: 23px; color: var(--name-red); line-height: 30px; margin-bottom: -2px;
  }
  .sender-line span + span { margin-left: 24px; }

  .services {
    position: absolute; left: 157px; top: 223px; width: 651px; height: 26px;
    border-top: 1px solid var(--rule); border-bottom: 1px solid var(--rule);
    display: flex; justify-content: space-between; align-items: center;
    list-style: none;
    font-family: "Arimo", Arial, sans-serif; font-weight: 700; font-size: 13.5px; color: var(--ink);
  }
  .services li { display: flex; align-items: center; padding-left: 12px; }
  .services li:last-child { padding-left: 0; }
  .services li::before {
    content: ""; width: 7px; height: 7px; background: var(--accent-red); margin-right: 9px;
  }
</style>
</head>
<body>
  <div class="letterhead">
    <div class="hex-pattern" role="img" aria-label="Wabenmuster aus roten und rosa Sechsecken"></div>
    <div class="dot-field" role="img" aria-label="Zartes graugrünes Punkteraster"></div>

    <header class="sender">
      <div class="sender-name">Valmor Keller</div>
      <div class="sender-line"><span>Eidg.dipl.Malermeister</span><span>Lindenweg 7</span><span>8810 Horgwil</span></div>
      <div>Telefon : 044 583 61 47</div>
      <div>Fax : 044 583 61 37</div>
      <div>Natel : 079 412 55 20</div>
      <div>Email : gutachten@valmorkeller.example</div>
    </header>

    <ul class="services">
      <li>Gutachten</li>
      <li>Expertisen</li>
      <li>Devisierungen</li>
      <li>Farbberatungen</li>
      <li>Dekorative Gestaltungen</li>
    </ul>
  </div>
</body>
</html>
```